Medical device engineering service firm needs an update to flier

We do engineering design work for medical products, from ideation through injection-molded prototypes. Our clients have assay that needs automation, or an idea that needs to be made concrete. We have a 2-sided flier that needs an update to the look. This flier is mainly used as both a take away at trade shows to describe our services and provide our contact information.

```html
<!DOCTYPE html>
<html lang="en">
<head>
<meta charset="utf-8">
<title>Veridan Product Development – Flier</title>
<link href="https://fonts.googleapis.com/css2?family=Roboto+Condensed:wght@400;700&family=Roboto:wght@400;500&family=Montserrat:wght@300;400&display=swap" rel="stylesheet">
<style>
:root{
  --purple:#7b2a80;
  --purple-dark:#5a1c5f;
  --green:#a8c14a;
  --green-dark:#8fa83a;
  --gray-bg:#dedede;
  --gray-panel:#e8e8e8;
  --shadow:#9a9a9a;
  --ink:#2e2e2e;
  --white:#ffffff;
}
*{box-sizing:border-box;margin:0;padding:0}
html,body{width:1200px;height:758px;overflow:hidden;background:var(--white)}
body{position:relative;font-family:"Roboto Condensed",Arial,sans-serif;color:var(--ink)}

.page{position:absolute;top:32px;width:538px;height:696px;background:var(--white);box-shadow:5px 5px 0 var(--shadow);overflow:hidden}
.page-front{left:44px;background:var(--gray-panel)}
.page-back{left:620px}

/* brand */
.brand{position:absolute;display:flex;align-items:center;gap:6px;color:var(--purple);font-family:"Roboto Condensed",sans-serif;font-weight:700;line-height:1}
.brand-dot{width:12px;height:12px;border-radius:50%;background:var(--green)}
.brand-name{font-size:26px}
.brand-sub{display:block;font-size:8px;letter-spacing:.4px;margin-top:2px}

/* front header */
.front-header{position:absolute;left:0;top:0;width:538px;height:78px;background:var(--white)}
.front-header svg{position:absolute;left:0;top:0}
.front-header .brand{left:26px;top:22px}
.front-title{position:absolute;left:206px;top:14px;color:var(--white);font-family:"Roboto Condensed",sans-serif;font-weight:400;font-size:18px;line-height:19px;letter-spacing:1px}

.hero{position:absolute;left:0;top:78px;width:538px;height:396px;background:linear-gradient(180deg,#7d3f85 0%,#6c2f74 55%,#4a4a4c 78%,#333336 100%)}
.hero-copy{position:absolute;left:20px;top:372px;width:505px;color:var(--white);font-family:"Roboto Condensed",sans-serif;font-size:9.4px;line-height:11.8px;text-shadow:0 0 3px rgba(0,0,0,.6)}

.front-headline{position:absolute;left:0;top:482px;width:538px;text-align:center;color:var(--purple);font-family:"Roboto Condensed",sans-serif;font-weight:700;font-size:17.5px;line-height:20px}

.offer-col{position:absolute;top:528px;width:154px;height:160px;background:var(--white)}
.offer-col h3{position:relative;height:21px;background:var(--green);color:var(--ink);font-family:"Roboto Condensed",sans-serif;font-weight:700;font-size:13px;line-height:21px;text-align:center}
.offer-col h3::after{content:"";position:absolute;left:50%;bottom:-6px;margin-left:-6px;border:6px solid transparent;border-bottom:0;border-top-color:var(--green)}
.offer-col ul{list-style:none;padding:9px 4px 0 6px;font-family:"Roboto Condensed",sans-serif;font-size:8.5px;line-height:11.4px}
.offer-col li::before{content:"• "}
.col-portfolio{left:18px}
.col-services{left:188px}
.col-capabilities{left:356px;width:164px}

/* back header */
.back-header{position:absolute;left:0;top:0;width:538px;height:120px}
.back-header svg{position:absolute;left:0;top:0}
.back-header .brand{left:26px;top:48px}
.back-kicker{position:absolute;left:227px;top:24px;color:var(--white);font-family:"Roboto Condensed",sans-serif;font-weight:400;font-size:20px}
.back-title{position:absolute;left:227px;top:52px;color:var(--white);font-family:"Roboto Condensed",sans-serif;font-weight:400;font-size:28.5px;line-height:31px}

.process{position:absolute;left:0;top:120px;width:538px;height:509px;background:var(--gray-bg)}
.phase{position:absolute;top:18px;width:91px;height:473px;background:var(--white);display:flex;flex-direction:column}
.phase-01{left:16px}.phase-02{left:122px;width:184px}.phase-03{left:324px}.phase-45{left:433px}
.phase-head{position:relative;height:64px;color:var(--white);padding:6px 0 0 13px;font-family:"Roboto Condensed",sans-serif;font-weight:700}
.phase-head .label{font-size:10px;letter-spacing:.3px}
.phase-head .num{font-size:46px;line-height:42px}
.phase-head .num small{font-size:22px}
.phase-head.purple{background:var(--purple)}
.phase-head.green{background:var(--green)}
.phase-02 .phase-head{padding-left:65px}
.phase-head::after{content:"";position:absolute;bottom:-6px;left:50%;margin-left:-6px;border:6px solid transparent;border-bottom:0}
.phase-head.purple::after{border-top-color:var(--purple)}
.phase-head.green::after{border-top-color:var(--green)}
.steps{flex:1;display:flex}
.step-stack{flex:1;display:flex;flex-direction:column}
.step-stack + .step-stack{border-left:1px solid #e4e4e4}
.step{flex:1;display:flex;flex-direction:column;align-items:center;padding-top:26px;position:relative}
.step + .step::before{content:"";position:absolute;top:0;left:8px;right:8px;height:1px;background:linear-gradient(90deg,transparent,#c9a6cc,transparent)}
.step svg{width:36px;height:36px}
.step p{margin-top:12px;padding:0 3px;font-family:"Roboto Condensed",sans-serif;font-size:8.4px;line-height:10.6px;text-align:center}
.ic-p{fill:none;stroke:var(--purple);stroke-width:3;stroke-linecap:round;stroke-linejoin:round}
.ic-g{fill:none;stroke:var(--green-dark);stroke-width:3;stroke-linecap:round;stroke-linejoin:round}
.fill-p{fill:var(--purple)}.fill-g{fill:var(--green-dark)}

.back-footer{position:absolute;left:0;top:629px;width:538px;height:67px;border-top:3px solid var(--green);background:var(--white)}
.address{position:absolute;left:36px;top:14px;font-family:"Montserrat",sans-serif;font-weight:300;font-size:12.5px;line-height:17px;letter-spacing:.6px;color:#444}
.footer-rule{position:absolute;left:222px;top:12px;width:1px;height:40px;background:#bbb}
.contact{position:absolute;left:236px;top:12px;font-family:"Montserrat",sans-serif;font-weight:400;font-size:15px;line-height:19px;letter-spacing:.8px;color:#333}
.cert-badge{position:absolute;left:476px;top:14px;width:34px;height:34px;border-radius:50%;background:#2f4f9a}
</style>
</head>
<body>

<section class="page page-front">
  <header class="front-header">
    <svg width="538" height="78" aria-hidden="true">
      <polygon points="196,0 538,0 538,78 180,78" fill="var(--green)"/>
      <polygon points="184,0 196,0 180,78 168,78" fill="var(--purple)"/>
    </svg>
    <div class="brand"><span class="brand-dot"></span><span><span class="brand-name">veridan</span><span class="brand-sub">PRODUCT DEVELOPMENT</span></span></div>
    <h1 class="front-title">RAPID Design<br>Engineering of Medical<br>Devices Specializing in Plastics</h1>
  </header>

  <div class="hero" role="img" aria-label="Photo of a businessman climbing stairs toward a bright doorway, with sketches of medical device parts and formulas on a purple wall"></div>
  <p class="hero-copy">Our highly experienced biomedical and mechanical engineers leverage our extensive in-house fabrication capabilities to create proven, manufacturable designs with unmatched speed, efficiency and quality. They have developed over 300 successful designs, forming our deep portfolio that has generated hundreds of millions of dollars for our clients. It includes FDA Class 1, II, and 11 devices, developed under our ISO 13485 certified quality management system.</p>

  <h2 class="front-headline">We specialize in design engineering and design-for-manufacturing<br>of innovative medical and life science devices that use plastics</h2>

  <div class="offer-col col-portfolio">
    <h3>Our Portfolio Includes</h3>
    <ul>
      <li>Diagnostics / Molecular Diagnostics</li>
      <li>Sample Collection / Preparation</li>
      <li>Life Science / Laboratory Products</li>
      <li>Microfluidics / Small Volume Handling</li>
      <li>Buffer &amp; Reagent Storage &amp; Delivery</li>
      <li>Surgical / Clinical Tools</li>
      <li>Drug Delivery Devices</li>
      <li>Electromechanical Devices</li>
      <li>Consumer and Industrial Products</li>
    </ul>
  </div>
  <div class="offer-col col-services">
    <h3>Our Services Include</h3>
    <ul>
      <li>Concept Development</li>
      <li>Engineering and Design</li>
      <li>Industrial Design</li>
      <li>Design for Manufacturing and Assembly</li>
      <li>Design Control per ISO 13485</li>
      <li>Finite Element Analysis (FEA)</li>
      <li>Design Verification Testing</li>
      <li>Test Method Development</li>
      <li>Test and Assembly Fixture Development</li>
      <li>Transfer to Manufacturing</li>
    </ul>
  </div>
  <div class="offer-col col-capabilities">
    <h3>Our In-House Capabilities</h3>
    <ul>
      <li>Stereolithography (SLA) Prototyping</li>
      <li>CNC Machining / Fabrication</li>
      <li>Prototype Mold Fabrication</li>
      <li>Prototype Injection Molding</li>
      <li>Liquid Injection Molded (LIM) Silicone Prototype Molding</li>
      <li>Injection Molding Simulation &amp; Analysis</li>
      <li>Product Reliability Testing</li>
      <li>Plastics Assembly Expertise</li>
      <li>Material Selection Expertise, Research and Testing</li>
    </ul>
  </div>
</section>

<section class="page page-back">
  <header class="back-header">
    <svg width="538" height="120" aria-hidden="true">
      <polygon points="208,0 538,0 538,120 180,120" fill="var(--purple)"/>
      <polygon points="196,0 208,0 180,120 168,120" fill="var(--green)"/>
    </svg>
    <div class="brand"><span class="brand-dot"></span><span><span class="brand-name">veridan</span><span class="brand-sub">PRODUCT DEVELOPMENT</span></span></div>
    <p class="back-kicker">Steps To Success</p>
    <h1 class="back-title">Our Medical Device<br>Development Process</h1>
  </header>

  <div class="process">
    <article class="phase phase-01">
      <div class="phase-head purple"><div class="label">PHASE</div><div class="num">01</div></div>
      <div class="steps"><div class="step-stack">
        <div class="step">
          <svg viewBox="0 0 36 36" aria-hidden="true"><path class="ic-p" d="M3 18 Q18 4 33 18 Q18 32 3 18Z"/><circle class="fill-p" cx="18" cy="18" r="6"/></svg>
          <p>Discuss your project needs. Estimate the work to accomplish your vision.</p>
        </div>
        <div class="step">
          <svg viewBox="0 0 36 36" aria-hidden="true"><circle class="ic-p" cx="16" cy="20" r="13"/><circle class="ic-p" cx="16" cy="20" r="7"/><circle class="fill-p" cx="16" cy="20" r="2.5"/><path class="ic-p" d="M16 20 L32 4"/></svg>
          <p>Define the product requirements, giving us a well-defined target for development.</p>
        </div>
        <div class="step">
          <svg viewBox="0 0 36 36" aria-hidden="true"><path class="fill-p" d="M18 3a10 10 0 0 0-6 18v4h12v-4a10 10 0 0 0-6-18z"/><rect class="fill-p" x="13" y="27" width="10" height="3" rx="1"/><rect class="fill-p" x="14" y="31" width="8" height="2.5" rx="1"/></svg>
          <p>Brainstorm solutions, drawing from the experience of our entire engineering team.</p>
        </div>
      </div></div>
    </article>

    <article class="phase phase-02">
      <div class="phase-head green"><div class="label">PHASE</div><div class="num">02</div></div>
      <div class="steps">
        <div class="step-stack">
          <div class="step">
            <svg viewBox="0 0 36 36" aria-hidden="true"><path class="fill-g" d="M15 3h6v11l7 17H8l7-17z"/></svg>
            <p>Develop concepts that provide an array of potential design solutions.</p>
          </div>
          <div class="step">
            <svg viewBox="0 0 36 36" aria-hidden="true"><rect class="ic-p" x="12" y="4" width="21" height="16"/><path class="ic-g" d="M4 33V22M8 14l8-3"/></svg>
            <p>Analyze and present concepts. Determine which one best meets all product requirements.</p>
          </div>
          <div class="step">
            <svg viewBox="0 0 36 36" aria-hidden="true"><rect class="ic-p" x="9" y="6" width="18" height="12"/><rect class="fill-g" x="3" y="24" width="30" height="5"/></svg>
            <p>Design all details in 3D CAD, defining tolerances, materials &amp; assembly methods.</p>
          </div>
        </div>
        <div class="step-stack">
          <div class="step">
            <svg viewBox="0 0 36 36" aria-hidden="true"><path class="ic-g" d="M8 26 A12 12 0 1 1 28 24"/><path class="ic-g" d="M22 24h7v-7"/></svg>
            <p>Individually prototype any functions that are likely to require iteration.</p>
          </div>
          <div class="step">
            <svg viewBox="0 0 36 36" aria-hidden="true"><path class="ic-g" d="M6 16A12 12 0 0 1 28 10"/><path class="ic-g" d="M30 20A12 12 0 0 1 8 26"/><path class="fill-g" d="M24 6l7 1-3 7z M12 30l-7-1 3-7z"/></svg>
            <p>Test prototypes against requirements. Quickly iterate with in-house prototyping.</p>
          </div>
          <div class="step">
            <svg viewBox="0 0 36 36" aria-hidden="true"><rect class="ic-g" x="6" y="4" width="20" height="27" rx="2"/><path class="ic-g" d="M11 12h10M11 18h10M11 24h5"/><circle class="fill-g" cx="27" cy="27" r="7"/><path d="M24 27l2 2 4-4" fill="none" stroke="#fff" stroke-width="2"/></svg>
            <p>Develop integrated prototype that combines all functions, and meets requirements.</p>
          </div>
        </div>
      </div>
    </article>

    <article class="phase phase-03">
      <div class="phase-head purple"><div class="label">PHASE</div><div class="num">03</div></div>
      <div class="steps"><div class="step-stack">
        <div class="step">
          <svg viewBox="0 0 36 36" aria-hidden="true"><path class="ic-p" d="M6 30L28 8M8 8l22 22"/><path class="fill-p" d="M4 4h8l-2 6-6-2z M26 4l6 6-3 3-6-6z"/></svg>
          <p>Fabricate prototype tooling in-house that we can easily iterate as needed.</p>
        </div>
        <div class="step">
          <svg viewBox="0 0 36 36" aria-hidden="true"><circle class="ic-p" cx="13" cy="22" r="7" stroke-dasharray="3 2" stroke-width="5"/><circle class="ic-p" cx="26" cy="10" r="5" stroke-dasharray="2.5 1.5" stroke-width="4"/></svg>
          <p>Mold and assemble fully functional, production quality devices.</p>
        </div>
        <div class="step">
          <svg viewBox="0 0 36 36" aria-hidden="true"><path class="ic-p" d="M6 16A12 12 0 0 1 28 10"/><path class="ic-p" d="M30 20A12 12 0 0 1 8 26"/><path class="fill-p" d="M24 6l7 1-3 7z M12 30l-7-1 3-7z"/></svg>
          <p>Test molded devices against requirements. Iterate molds as needed.</p>
        </div>
      </div></div>
    </article>

    <article class="phase phase-45">
      <div class="phase-head green"><div class="label">PHASE</div><div class="num">4<small>&amp;</small>5</div></div>
      <div class="steps"><div class="step-stack">
        <div class="step">
          <svg viewBox="0 0 36 36" aria-hidden="true"><circle class="ic-g" cx="14" cy="14" r="10"/><path class="ic-g" d="M21 21l10 10M9 14l4 4 6-7"/></svg>
          <p>Perform Design Verification Testing to confirming that all designs requirements are met.</p>
        </div>
        <div class="step">
          <svg viewBox="0 0 36 36" aria-hidden="true"><circle class="ic-g" cx="11" cy="13" r="6" stroke-dasharray="3 2" stroke-width="4"/><rect class="ic-g" x="19" y="17" width="13" height="16"/><path class="ic-g" d="M22 23h7M22 28h7"/></svg>
          <p>Seamlessly transfer to manufacturing for production scale up.</p>
        </div>
        <div class="step">
          <svg viewBox="0 0 36 36" aria-hidden="true"><rect class="ic-g" x="5" y="4" width="20" height="25"/><rect class="ic-g" x="10" y="8" width="20" height="25" fill="#fff"/><path class="ic-g" d="M14 20l4 5 12-14"/></svg>
          <p>Support patent and regulatory approval processes.</p>
        </div>
      </div></div>
    </article>
  </div>

  <footer class="back-footer">
    <p class="address">2240 Harbor Ridge Lane<br>Oceanview, CA 92000</p>
    <span class="footer-rule"></span>
    <p class="contact">VeridanPD.com<br>+1 555 014 2290</p>
    <span class="cert-badge" role="img" aria-label="Quality certification badge"></span>
  </footer>
</section>

</body>
</html>
```